Top Real Estate teams new cards UPDATED

New Cards with MY (Im the tall guy in the middle) new pic on the front of card and my team pic on the back of card. Also my team name on the front of the card (marlow and partners) and brokerage name on the back (harborline real estate group) . Also the tag line "Ask about our 20 step plan" on the back of the card and "Welcome to the new way of Real Estate Sales" on the front of the card along with my phone number (951-482-3067) and email address (derek.marlow47@quillmail.net) my website (www.DerekMarlow.org) and my License number (BRE:07315294). I do like my team name colors of black and gold
Logo links are attached:
1. https://www.filevaultly.net/sh/815kqwz73hpadrx/AAG7MmK2PlR4ZqWsYnUuE_HQb?dl=0
2. https://www.filevaultly.net/sh/29c7vxm84tq015r/AACKDRLW46NeT2Gh8Vr4Jk7Yb?dl=0
Updates

Target Market(s)

Real Estate Customers

Industry/Entity Type

Real Estate

Contact Information for Business Card

Classy, yet east ro read and understand

Font styles to use
Sans Serif

Requirements
Must have
• Team and brokerage name, and both slogans.
• Black and gold color scheme.
Nice to have
• Bold writing
Should not have
• cluttered feeling

```html
<!DOCTYPE html>
<html lang="en">
<head>
<meta charset="utf-8">
<title>Marlow and Partners – Business Card</title>
<link href="https://fonts.googleapis.com/css2?family=Cabin:wght@400;500&family=Montserrat:wght@700;800&display=swap" rel="stylesheet">
<style>
  :root {
    --page: #ffffff;
    --card: #000000;
    --gold: #fde29a;
    --gold-deep: #c9a45a;
    --label: #9a9a9a;
    --white: #ffffff;
    --photo-light: #b8b8b8;
    --photo-dark: #6f6f6f;
  }
  html, body {
    margin: 0;
    padding: 0;
    width: 1200px;
    height: 1200px;
    overflow: hidden;
    background: var(--page);
  }
  .canvas {
    position: relative;
    width: 1200px;
    height: 1200px;
  }
  .side-label {
    position: absolute;
    font-family: "Montserrat", sans-serif;
    font-weight: 800;
    font-size: 25px;
    color: var(--label);
    letter-spacing: 0.5px;
    margin: 0;
  }
  .side-label--front { left: 219px; top: 232px; }
  .side-label--back { left: 230px; top: 700px; }

  .card {
    position: absolute;
    left: 333px;
    width: 606px;
    height: 346px;
    background: var(--card);
    overflow: hidden;
  }
  .card--front { top: 238px; }
  .card--back { top: 706px; }

  /* Front */
  .welcome {
    position: absolute;
    left: 51px;
    top: 70px;
    width: 206px;
    text-align: center;
    font-family: "Cabin", sans-serif;
    color: var(--white);
  }
  .welcome__title {
    display: block;
    font-size: 38px;
    font-weight: 400;
    line-height: 38px;
    letter-spacing: 0.5px;
  }
  .welcome__lead {
    display: flex;
    align-items: center;
    gap: 6px;
    font-size: 12.5px;
    line-height: 14px;
    margin-top: 2px;
  }
  .welcome__lead::before,
  .welcome__lead::after {
    content: "";
    flex: 1;
    height: 2px;
    background: var(--white);
  }
  .welcome__subject {
    display: block;
    color: var(--gold);
    font-size: 26px;
    line-height: 30px;
    font-weight: 500;
    margin-top: 1px;
  }
  .gold-band {
    position: absolute;
    left: 0;
    width: 257px;
    height: 21px;
  }
  .gold-band--top { top: 182px; }
  .gold-band--bottom { top: 284px; }

  .team-name {
    position: absolute;
    left: 0;
    top: 214px;
    width: 300px;
    margin: 0;
    text-align: center;
    font-family: "Montserrat", sans-serif;
    font-weight: 800;
    font-size: 26px;
    line-height: 32px;
    color: var(--gold);
    letter-spacing: 0.3px;
    text-transform: uppercase;
  }
  .portrait {
    position: absolute;
    left: 361px;
    top: 32px;
    width: 181px;
    height: 181px;
    border-radius: 50%;
    background: radial-gradient(circle at 50% 40%, var(--photo-light), var(--photo-dark));
  }
  .contact {
    position: absolute;
    left: 370px;
    top: 231px;
    height: 74px;
    padding-left: 13px;
    border-left: 1.5px solid var(--white);
    font-family: "Cabin", sans-serif;
    font-size: 13px;
    line-height: 19.6px;
    color: var(--white);
    list-style: none;
    margin: 0;
  }
  .contact li { margin: 0; padding: 0; }

  /* Back */
  .brokerage {
    position: absolute;
    left: 404px;
    top: 34px;
    width: 128px;
    text-align: center;
    font-family: "Cabin", sans-serif;
    font-weight: 400;
    font-size: 11px;
    line-height: 14px;
    color: var(--white);
  }
  .plan {
    position: absolute;
    left: 80px;
    top: 88px;
    width: 216px;
    text-align: center;
  }
  .plan__ask {
    display: block;
    font-family: "Montserrat", sans-serif;
    font-weight: 700;
    font-size: 15px;
    letter-spacing: 3.6px;
    color: var(--white);
    line-height: 18px;
  }
  .plan__number {
    display: block;
    width: 216px;
    height: 128px;
  }
  .plan__label {
    display: block;
    font-family: "Montserrat", sans-serif;
    font-weight: 800;
    font-size: 29px;
    line-height: 32px;
    color: var(--gold);
    margin-top: 0;
  }
  .team-photo {
    position: absolute;
    left: 367px;
    top: 82px;
    width: 203px;
    height: 204px;
    background: radial-gradient(ellipse at 50% 35%, #c4c4c4, #6b6b6b);
  }
</style>
</head>
<body>
<div class="canvas">
  <p class="side-label side-label--front">FRONT</p>
  <section class="card card--front">
    <div class="welcome">
      <span class="welcome__title">WELCOME</span>
      <span class="welcome__lead">to the new way of</span>
      <span class="welcome__subject">Real Estate Sales</span>
    </div>

    <svg class="gold-band gold-band--top" viewBox="0 0 257 21" preserveAspectRatio="none">
      <rect width="257" height="21" fill="var(--gold)"/>
      <polygon points="0,0 80,0 60,21 0,21" fill="var(--gold-deep)" opacity="0.55"/>
    </svg>
    <h1 class="team-name">Marlow and<br>Partners</h1>
    <svg class="gold-band gold-band--bottom" viewBox="0 0 257 21" preserveAspectRatio="none">
      <rect width="257" height="21" fill="var(--gold)"/>
      <polygon points="0,0 80,0 60,21 0,21" fill="var(--gold-deep)" opacity="0.55"/>
    </svg>

    <div class="portrait" role="img" aria-label="Portrait photo of Derek Marlow in a dark suit"></div>

    <ul class="contact">
      <li>951-482-3067</li>
      <li>www.DerekMarlow.org</li>
      <li>derek.marlow47@quillmail.net</li>
      <li>BRE: 07315294</li>
    </ul>
  </section>

  <p class="side-label side-label--back">BACK</p>
  <section class="card card--back">
    <p class="brokerage">Harborline<br>Real Estate Group</p>

    <div class="plan">
      <span class="plan__ask">ASK ABOUT OUR</span>
      <svg class="plan__number" viewBox="0 0 216 128" aria-label="20">
        <defs>
          <linearGradient id="goldFoil" x1="0" y1="0" x2="1" y2="1">
            <stop offset="0" stop-color="#fbe6a6"/>
            <stop offset="0.45" stop-color="#d9b868"/>
            <stop offset="0.7" stop-color="#f3d889"/>
            <stop offset="1" stop-color="#a8863e"/>
          </linearGradient>
        </defs>
        <text x="108" y="122" text-anchor="middle" font-family="Montserrat, sans-serif" font-weight="800" font-size="164" letter-spacing="-6" fill="url(#goldFoil)">20</text>
      </svg>
      <span class="plan__label">STEP PLAN</span>
    </div>

    <div class="team-photo" role="img" aria-label="Team photo of three agents in black outfits"></div>
  </section>
</div>
</body>
</html>
```